Packaged Food Business Needs a Packaging Design

We need a package design to be used as a label/sticker on the lids of round and square transparent plastic containers and on the sides of resealable stand-up pouches. The brand name is 'Tastora' - please find attached logo together with pictures of the sample containers and pouch. We will use the packaging to market a wide variety of food categories from nuts, dried fruits, spices, cooking chocolates, baking ingredients, cereals, grains and pulses.

OVERALL FEEDBACK ON DESIGNS ALREADY RECEIVED:

- We have found so far that a lot of our mandatory requirements are not adhered to in designs that have been submitted so far. We would like to emphasise that the ingredient, weight and expiry text will be printed at the time of packing so it should not take prime space on the pack BUT at the same time some 'blank' space needs to flawlessly be incorporated into the overall design for this purpose
- We encourage you to glorify the brand logo in the pack, and absolutely refrain from duplicating the tagline
- Please note that ONE label design will be used to pack a wide variety of food ingredients and therefore please ensure that the choice of your design incorporates this requirement, in the past we have received designs that are limited to only one type of food (like nuts) or have received designs that are too floral or leafy (and not grounded to food
- Please ensure that you submit designs for all three packaging formats, it is critical to see the family look from the on-set

Target Market(s)

The brand is targeting both mothers and professional chefs and therefore the label design should be broadly approachable and convey affordable premium

Industry/Entity Type

Business

Requirements
Must have
• - Consistent with the brand name and logo, the overall look and feel of the packaging should convey values of healthy, gourmet food ingredients, high in nourishment and project a sense of delightful taste
• - The design styling to be modern and 'simplistic' (embracing 'less-is-more' type of a design style)
• - Design a packaging architecture that incorporates the brand logo together with its tagline lock-up of 'savour the goodness in every morsel' - find logo attached
• - The design needs to have a dedicated area to print the ingredient (e.g., Mixed Nuts), weight (e.g., 500g) and expiry (this space needs to be flawlessly incorporated into the design) - this information will be printed either with an inkjet printer or with a rubber stamp so please leave an empty space (the text should not be part of the design, just the area for the text needs to be included in the design)
• - The packaging must include 'Packed By: Kelvane Distributors Ltd, P. O. Box 51946, Kampala - Uganda'
• - For the design of the resealable pouch, please incorporate a window to see through the ingredients and a hole on top to hang on supermarket pegs if necessary
Nice to have
• - We would love to have some design submissions that are bold and cheerful and fun (but not frivolous) - please see attached inspiration for 'fun' packaging. The attachments are purely for inspiration, not to infringe on anyone else's TM and copyrights
• - Incorporate green to convey healthy, organic values
• - Explore use of gold and silver convey premiumness
Should not have
• - Do not duplicate the tagline
• - Do not include the ingredient, weight and expiry in the main graphic of the design, these will be printed at the time of packing so ensure there is provision for this in a flawless way in the design (e.g., via a blank space allocated for this purpose)

```html
<!DOCTYPE html>
<html lang="en">
<head>
<meta charset="utf-8">
<title>Tastora – Label System</title>
<link rel="stylesheet" href="https://fonts.googleapis.com/css2?family=Alegreya:ital,wght@0,400;1,400&family=Oswald:wght@600&family=Questrial&display=swap">
<style>
  :root{
    --ink:#444;
    --rule:#9a9a9a;
    --brand-brown:#3b1e10;
    --tag-orange:#b0601e;
    --gold:#e0ad4a;
    --sun-yellow:#f6d81c;
    --green:#3a9f3e;
    --blue:#29a8e0;
    --orange:#f05a28;
    --choc:#3d1f0f;
    --pink:#e6178a;
    --purple:#6b2d8f;
    --footer:#e6e6e6;
  }
  *{margin:0;padding:0;box-sizing:border-box}
  html,body{width:1200px;height:1068px;overflow:hidden;background:#fff}
  .sheet{position:relative;width:1200px;height:1068px}
  .section-title{position:absolute;font-family:"Questrial",sans-serif;font-weight:400;font-size:15px;letter-spacing:1px;color:var(--ink);text-align:center;line-height:19px;text-transform:uppercase}
  .section-title small{font-size:15px;text-transform:none}
  .rule{position:absolute;height:1px;background:var(--rule)}
  .note{position:absolute;left:8px;top:362px;width:74px;font-family:"Questrial",sans-serif;font-size:11px;line-height:11px;color:var(--ink);text-align:center}
  .artboard{position:absolute;left:0;top:0}
  .footer-band{position:absolute;left:0;top:1005px;width:1200px;height:63px;background:var(--footer)}
  .logo-word{font-family:"Oswald",sans-serif;font-weight:600;fill:var(--brand-brown);letter-spacing:4px}
  .tagline{font-family:"Alegreya",serif;font-style:italic;fill:var(--tag-orange)}
  .packed{font-family:"Alegreya",serif;font-style:italic;fill:#333}
  .badge-text{font-family:"Alegreya",serif;font-style:italic;fill:#fff}
</style>
</head>
<body>
<main class="sheet">
  <h2 class="section-title" style="left:98px;top:58px;width:200px">Mother Label</h2>
  <h2 class="section-title" style="left:324px;top:38px;width:200px">Category Labels<br><small>(Examples)</small></h2>
  <div class="rule" style="left:57px;top:84px;width:461px"></div>
  <h2 class="section-title" style="left:686px;top:58px;width:340px">Labeling Preview <small>(Examples)</small></h2>
  <div class="rule" style="left:570px;top:84px;width:577px"></div>
  <h2 class="section-title" style="left:400px;top:490px;width:400px">Variety Packaging Preview</h2>
  <div class="rule" style="left:44px;top:516px;width:1112px"></div>
  <p class="note">Space for aditional information</p>

  <svg class="artboard" width="1200" height="1068" viewBox="0 0 1200 1068" xmlns="http://www.w3.org/2000/svg">
    <defs>
      <clipPath id="label-clip"><path d="M0,100 A100,100 0 0 1 200,100 L200,362 L100,340 L0,362 Z"/></clipPath>
      <linearGradient id="frost" x1="0" y1="0" x2="0" y2="1">
        <stop offset="0" stop-color="#f4f4f4"/><stop offset="1" stop-color="#e4e4e4"/>
      </linearGradient>
      <symbol id="label" viewBox="0 0 200 362">
        <path d="M0,100 A100,100 0 0 1 200,100 L200,362 L100,340 L0,362 Z" fill="#fff"/>
        <g clip-path="url(#label-clip)">
          <path role="img" aria-label="Illustrated savanna scene with acacia tree, mountains and crowned crane over a golden grain pattern" d="M0,140 Q30,126 60,136 Q100,128 130,138 Q170,124 200,134 L200,280 Q160,292 120,280 Q80,292 50,282 Q20,290 0,284 Z" fill="var(--sun-yellow)"/>
        </g>
        <path d="M3,100 A97,97 0 0 1 197,100 L197,357 L100,336 L3,357 Z" fill="none" stroke="var(--gold)" stroke-width="1.2"/>
        <text class="logo-word" x="100" y="94" font-size="36" text-anchor="middle">TASTORA</text>
        <text class="tagline" x="100" y="120" font-size="11.5" text-anchor="middle">savour the goodness in every morsel</text>
        <text class="packed" x="10" y="320" font-size="6.5">Packed By:</text>
        <text class="packed" x="10" y="328" font-size="6.5">Kelvane Distributors Ltd, P. O. Box 51946,</text>
        <text class="packed" x="10" y="336" font-size="6.5">Kampala - Uganda</text>
      </symbol>
      <symbol id="badge-ring" viewBox="-36 -36 72 72">
        <circle r="35" fill="currentColor" stroke="#fff" stroke-width="1" stroke-dasharray="3 2"/>
        <circle r="30" fill="none" stroke="var(--gold)" stroke-width="0.8"/>
      </symbol>
    </defs>

    <use href="#label" x="88" y="100" width="200" height="362"/>
    <path d="M84,357 H80 V405 H84" fill="none" stroke="#777" stroke-width="0.8"/>

    <g class="badge" transform="translate(382,180)">
      <use href="#badge-ring" x="-36" y="-36" width="72" height="72" style="color:var(--green)"/>
      <text class="badge-text" y="-3" font-size="15" text-anchor="middle">Mixed</text>
      <text class="badge-text" y="12" font-size="15" text-anchor="middle">Nuts</text>
    </g>
    <g class="badge" transform="translate(468,180)">
      <use href="#badge-ring" x="-36" y="-36" width="72" height="72" style="color:var(--blue)"/>
      <text class="badge-text" y="-3" font-size="15" text-anchor="middle">For</text>
      <text class="badge-text" y="12" font-size="15" text-anchor="middle">Baking</text>
    </g>
    <g class="badge" transform="translate(382,264)">
      <use href="#badge-ring" x="-36" y="-36" width="72" height="72" style="color:var(--orange)"/>
      <text class="badge-text" y="5" font-size="15" text-anchor="middle">Nuts</text>
    </g>
    <g class="badge" transform="translate(468,264)">
      <use href="#badge-ring" x="-36" y="-36" width="72" height="72" style="color:var(--choc)"/>
      <text class="badge-text" y="5" font-size="14" text-anchor="middle">Chocolate</text>
    </g>
    <g class="badge" transform="translate(382,353)">
      <use href="#badge-ring" x="-36" y="-36" width="72" height="72" style="color:var(--pink)"/>
      <text class="badge-text" y="5" font-size="15" text-anchor="middle">Peanuts</text>
    </g>
    <g class="badge" transform="translate(468,353)">
      <use href="#badge-ring" x="-36" y="-36" width="72" height="72" style="color:var(--purple)"/>
      <text class="badge-text" y="5" font-size="15" text-anchor="middle">Cereal</text>
    </g>

    <line x1="541" y1="120" x2="541" y2="443" stroke="#999" stroke-width="1" stroke-dasharray="2 2"/>

    <use href="#label" x="610" y="155" width="134" height="243"/>
    <g class="badge" transform="translate(735,352)">
      <use href="#badge-ring" x="-34" y="-34" width="68" height="68" style="color:var(--green)"/>
      <text class="badge-text" y="-3" font-size="14" text-anchor="middle">Mixed</text>
      <text class="badge-text" y="11" font-size="14" text-anchor="middle">Nuts</text>
    </g>
    <use href="#label" x="792" y="155" width="134" height="243"/>
    <g class="badge" transform="translate(917,352)">
      <use href="#badge-ring" x="-34" y="-34" width="68" height="68" style="color:var(--orange)"/>
      <text class="badge-text" y="5" font-size="14" text-anchor="middle">Nuts</text>
    </g>
    <use href="#label" x="974" y="155" width="134" height="243"/>
    <g class="badge" transform="translate(1099,352)">
      <use href="#badge-ring" x="-34" y="-34" width="68" height="68" style="color:var(--pink)"/>
      <text class="badge-text" y="5" font-size="14" text-anchor="middle">Peanuts</text>
    </g>

    <g class="pouch">
      <rect x="56" y="578" width="206" height="332" rx="6" fill="url(#frost)" stroke="#ddd"/>
      <rect x="56" y="578" width="206" height="22" fill="#ebebeb"/>
      <rect x="72" y="630" width="174" height="250" rx="30" fill="#c8955a" opacity="0.55" role="img" aria-label="Baked nut cookies seen through the clear pouch"/>
      <use href="#label" x="107" y="665" width="105" height="190"/>
      <g transform="translate(205,818)">
        <use href="#badge-ring" x="-27" y="-27" width="54" height="54" style="color:var(--orange)"/>
        <text class="badge-text" y="4" font-size="11" text-anchor="middle">Nuts</text>
      </g>
    </g>

    <g class="pouch">
      <rect x="304" y="578" width="206" height="332" rx="6" fill="url(#frost)" stroke="#ddd"/>
      <rect x="304" y="578" width="206" height="22" fill="#ebebeb"/>
      <rect x="320" y="630" width="174" height="250" rx="30" fill="#6e5632" opacity="0.55" role="img" aria-label="Seeded cereal bites seen through the clear pouch"/>
      <use href="#label" x="355" y="665" width="105" height="190"/>
      <g transform="translate(453,818)">
        <use href="#badge-ring" x="-27" y="-27" width="54" height="54" style="color:var(--purple)"/>
        <text class="badge-text" y="4" font-size="11" text-anchor="middle">Cereal</text>
      </g>
    </g>

    <g class="pouch">
      <rect x="578" y="588" width="219" height="329" rx="5" fill="#fafafa" stroke="#ddd"/>
      <rect x="578" y="588" width="219" height="24" fill="#f1f1f1"/>
      <circle cx="689" cy="604" r="7" fill="#fff" stroke="#ccc"/>
      <rect x="590" y="783" width="195" height="77" rx="4" fill="#b8875a" role="img" aria-label="Mixed nuts visible through the pouch window"/>
      <use href="#label" x="636" y="652" width="119" height="216"/>
      <g transform="translate(732,810)">
        <use href="#badge-ring" x="-30" y="-30" width="60" height="60" style="color:var(--green)"/>
        <text class="badge-text" y="-2" font-size="12" text-anchor="middle">Mixed</text>
        <text class="badge-text" y="10" font-size="12" text-anchor="middle">Nuts</text>
      </g>
    </g>

    <g class="tub">
      <rect x="860" y="840" width="262" height="85" rx="18" fill="#f2f2f2" stroke="#ddd"/>
      <rect x="848" y="768" width="285" height="104" rx="22" fill="#fbfbfb" stroke="#d8d8d8"/>
      <use href="#label" x="965" y="774" width="50" height="91"/>
      <g transform="translate(1008,845)">
        <use href="#badge-ring" x="-12" y="-12" width="24" height="24" style="color:var(--blue)"/>
        <text class="badge-text" y="-1" font-size="5" text-anchor="middle">For</text>
        <text class="badge-text" y="5" font-size="5" text-anchor="middle">Baking</text>
      </g>
    </g>
  </svg>

  <div class="footer-band"></div>
</main>
</body>
</html>
```